Website To Serve As A Resource For Medical Conditions

I need a website that is attractive that will be utilized to educate patients on either hepatitis c or HIV so it should be easily readable attractive but also professional. This website is going to be furnished with various topics for example, HIV treatment, HIV and Nutrition, HIV and Exercise, HIV and....

This website will also be cloned and utilized similarly for Hepatitis.

Coded - Design and coding required

1 page

0094D4
00A9DD
6FCCEA
C7EBF8
E9F6FB
A7469A
B969AE
D3A5CF
EDDBEB
F8F0F9
6B429C
8869AF
B7A5CE
E3DAEB
F3F0F8

```html
<!DOCTYPE html>
<html lang="en">
<head>
<meta charset="utf-8">
<title>Inform HIV – Patient Education</title>
<link href="https://fonts.googleapis.com/css2?family=Outfit:wght@500;600;700;800&family=Roboto:wght@400;500;700&display=swap" rel="stylesheet">
<style>
:root{
  --purple:#6B429C;
  --purple-mid:#8869AF;
  --magenta:#A7469A;
  --magenta-light:#B969AE;
  --lilac:#D3A5CF;
  --blush:#F3EDF4;
  --mist:#F8F0F9;
  --ink:#111111;
  --text:#444444;
  --muted:#777777;
  --hero-bg:#EFEFEF;
  --field:#EEEEEE;
  --line:#E3E3E3;
  --footer:#1B1228;
  --white:#ffffff;
}
*{box-sizing:border-box;margin:0;padding:0}
html,body{width:1200px;height:5063px;overflow:hidden}
body{font-family:'Roboto',sans-serif;color:var(--text);background:var(--white);position:relative}
.abs{position:absolute}
section,header,footer{position:absolute;left:0;width:1200px}
h1,h2,h3,.display{font-family:'Outfit',sans-serif;color:var(--ink);font-weight:800}
.btn{position:absolute;display:flex;align-items:center;justify-content:center;gap:6px;font-family:'Outfit',sans-serif;font-weight:700;font-size:12px;letter-spacing:.3px;text-transform:uppercase;background:var(--purple);color:var(--white)}
.btn-outline{background:transparent;border:2px solid var(--purple);color:var(--purple)}
.photo{position:absolute}
.para{position:absolute;font-size:16px;line-height:30px;color:var(--text)}

/* header */
.site-header{top:0;height:90px;z-index:5}
.brand{position:absolute;left:85px;top:18px;display:flex;align-items:center;gap:10px}
.brand-mark{width:40px;height:40px;background:var(--purple);border-radius:4px}
.brand-name{font-family:'Outfit',sans-serif;font-weight:700;font-size:15px;line-height:17px;color:var(--ink)}
.brand-name b{display:block;font-size:28px;line-height:28px;font-weight:700}
.nav a{position:absolute;top:37px;font-family:'Outfit',sans-serif;font-weight:600;font-size:13px;color:var(--ink);text-decoration:none}
.contact-btn{left:947px;top:24px;width:155px;height:45px}

/* hero */
.hero{top:0;height:620px;background:var(--hero-bg)}
.hero h1{position:absolute;left:85px;top:192px;font-size:58px;line-height:61px;letter-spacing:.3px}
.hero h1 span{color:var(--magenta)}
.hero .para{left:85px;top:396px;width:420px;font-size:17px;line-height:29px}
.hero .btn{left:85px;top:481px;width:158px;height:53px}
.hero-photo{left:610px;top:80px;width:590px;height:540px;background:linear-gradient(135deg,#e9e6ea 0%,#d9d2dc 45%,#9b5aa6 75%,#6B429C 100%)}
.badge{position:absolute;border-radius:50%;background:linear-gradient(135deg,var(--magenta),var(--purple));color:var(--white);display:flex;flex-direction:column;align-items:center;justify-content:center;text-align:center;font-family:'Outfit',sans-serif;font-weight:700;text-transform:uppercase;border:4px solid var(--white);box-shadow:0 0 0 2px var(--lilac)}
.hero .badge{left:538px;top:475px;width:114px;height:114px;font-size:15px;line-height:20px}
.hero .badge small{font-size:12px;font-weight:500}
.dot{position:absolute;border-radius:50%;background:var(--purple)}

/* stats */
.stats{top:620px;height:156px;background:#fbfbfb}
.stat-icon{position:absolute;top:42px;width:78px;height:80px;background:var(--white);box-shadow:4px 4px 0 #ececec;display:flex;align-items:center;justify-content:center}
.stat-num{position:absolute;top:38px;font-family:'Outfit',sans-serif;font-weight:800;font-size:46px;line-height:52px;color:var(--magenta)}
.stat-label{position:absolute;top:96px;font-size:18px;color:var(--ink)}

/* about */
.about{top:776px;height:314px}
.eyebrow-line{left:85px;top:78px;width:92px;height:1px;background:var(--ink)}
.eyebrow{left:190px;top:68px;font-size:15px;font-weight:500;color:var(--ink)}
.about h2{position:absolute;left:85px;top:96px;font-size:41px;line-height:48px}
.about .para{left:536px;top:63px;width:580px}

/* treatment */
.treatment{top:1090px;height:610px}
.frame{position:absolute;border:7px solid var(--purple)}
.treatment .frame{left:85px;top:318px;width:158px;height:199px}
.treatment .photo{left:112px;top:8px;width:456px;height:483px;background:linear-gradient(135deg,#dcdcdc,#c8c8c8 55%,#d8b5a3 75%,#cc2f2f)}
.treatment h2{position:absolute;left:640px;top:80px;font-size:42px;line-height:52px}
.treatment .para{left:642px;top:146px;width:474px}
.treatment .btn{left:642px;top:358px;width:148px;height:49px}

/* nutrition */
.nutrition{top:1699px;height:576px;background:var(--blush)}
.nutrition .badge{left:249px;top:82px;width:122px;height:122px;font-size:15px;line-height:22px}
.nutrition .badge small{font-size:12px;font-weight:500}
.nutrition h2{position:absolute;left:94px;width:433px;text-align:center;top:224px;font-size:43px;line-height:52px}
.nutrition .para{left:90px;top:290px;width:440px;text-align:center}
.nutrition .btn{left:238px;top:442px;width:145px;height:47px}
.nutrition-photo{left:540px;top:-29px;width:660px;height:605px;background:linear-gradient(135deg,#f0e6df 0%,#e9d2a6 40%,#d9a06b 60%,#a24fa0 85%,#6B429C 100%)}

/* exercise */
.exercise{top:2275px;height:891px}
.exercise h2{position:absolute;left:83px;top:82px;font-size:43px;line-height:52px}
.exercise .para{left:85px;top:149px;width:460px}
.exercise .btn{left:966px;top:92px;width:148px;height:49px}
.exercise-photo{left:85px;top:239px;width:465px;height:556px;background:linear-gradient(160deg,#ececec,#d6d6d6 55%,#7fb6c8 85%,#8ec6d6)}
.daily{position:absolute;left:85px;top:239px;width:233px;height:147px;background:var(--magenta);display:flex;align-items:center;gap:14px;padding-left:20px;color:var(--white);font-family:'Outfit',sans-serif;font-weight:700;text-transform:uppercase;font-size:15px;line-height:23px}
.daily small{font-size:12px;font-weight:600}
.check-list{position:absolute;left:599px;top:232px;width:515px;list-style:none}
.check-list li{position:relative;height:104px;padding:14px 20px 0 60px;font-size:16px;line-height:29px;color:var(--text);border-bottom:1px solid var(--line)}
.check-list li:last-child{border-bottom:none}
.check-list .arrow{position:absolute;left:0;top:18px;width:40px;height:40px;border-radius:50%;background:var(--purple);display:flex;align-items:center;justify-content:center}

/* mentors */
.mentors{top:3166px;height:624px;background:linear-gradient(100deg,var(--purple) 0%,#7d449f 55%,var(--magenta) 100%);color:var(--white)}
.mentors h2{position:absolute;left:0;width:1200px;text-align:center;top:84px;font-size:44px;line-height:52px;color:var(--white)}
.mentors .lead{position:absolute;left:0;width:1200px;text-align:center;top:158px;font-size:17px;line-height:31px;color:#f0e6f4}
.mentor{position:absolute;top:266px;width:220px;text-align:center}
.avatar-ring{margin:0 auto;width:170px;height:170px;border-radius:50%;border:2px dotted rgba(255,255,255,.85);display:flex;align-items:center;justify-content:center}
.avatar{width:152px;height:152px;border-radius:50%;background:linear-gradient(180deg,#e8e4ea,#cfc7d3)}
.mentor-name{margin-top:22px;font-family:'Outfit',sans-serif;font-weight:700;font-size:21px;color:var(--white)}
.mentor-role{margin-top:6px;font-size:17px;color:#f3eaf6}
.mentor-rule{margin:12px auto 0;width:30px;height:4px;background:var(--white)}
.slider-arrow{position:absolute;top:326px}

/* consult */
.consult{top:3790px;height:770px}
.consult .frame{left:85px;top:91px;width:184px;height:312px}
.consult .photo{left:116px;top:120px;width:361px;height:336px;background:linear-gradient(180deg,#d7d7d7,#c4c4c4 60%,#eaeaea)}
.consult h2{position:absolute;left:85px;top:503px;font-size:43px;line-height:49px}
.consult .para{left:85px;top:631px;width:450px;font-size:17px}
.form-card{position:absolute;left:599px;top:91px;width:515px;height:589px;background:var(--white);box-shadow:0 6px 34px rgba(0,0,0,.09)}
.field-label{position:absolute;font-family:'Outfit',sans-serif;font-weight:700;font-size:14px;color:var(--ink);text-transform:uppercase}
.field{position:absolute;background:var(--field);font-size:15px;color:#888;padding-left:18px;display:flex;align-items:center}
.field.area{align-items:flex-start;padding-top:14px}
.form-card .btn{left:175px;top:499px;width:165px;height:49px}

/* footer */
.site-footer{top:4560px;height:503px;background:var(--footer);color:#9a93a6}
.site-footer .brand{left:98px;top:112px}
.site-footer .brand-name{color:var(--white)}
.social{position:absolute;top:199px;width:50px;height:50px;border-radius:50%;border:1px solid #3a3048;background:#241a33}
.foot-title{position:absolute;top:89px;font-family:'Outfit',sans-serif;font-weight:700;font-size:21px;color:var(--white)}
.foot-links a,.foot-text{position:absolute;font-size:17px;color:#9a93a6;text-decoration:none;line-height:27px}
.foot-icon{position:absolute}
.news-field{position:absolute;left:841px;top:219px;width:273px;height:47px;background:#2b2239;display:flex;align-items:center;padding-left:20px;gap:14px;font-size:16px;color:#8a8296}
.foot-rule{position:absolute;left:0;top:390px;width:1200px;height:1px;background:#2c233a}
.copyright{position:absolute;left:0;width:1200px;top:452px;text-align:center;font-size:14px;font-weight:700;color:var(--white)}
.to-top{position:absolute;left:1129px;top:399px;width:48px;height:48px;border-radius:50%;background:var(--purple);display:flex;align-items:center;justify-content:center}
</style>
</head>
<body>

<section class="hero">
  <div class="photo hero-photo" role="img" aria-label="Doctor explaining treatment notes on a clipboard to a smiling patient, with purple geometric shapes behind"></div>
  <div class="dot" style="left:1102px;top:197px;width:42px;height:42px"></div>
  <h1>Educate The<br><span>Patients</span> on HIV<br>Treatment.</h1>
  <p class="para">Excepteur sint occaecat cupidatat non proident sunt in culpa mollit.</p>
  <a class="btn">Get Started &rarr;</a>
  <div class="badge">Bring<small>Your Ideas</small>To Life</div>
</section>

<header class="site-header">
  <div class="brand"><span class="brand-mark"></span><span class="brand-name">Inform<b>HIV</b></span></div>
  <nav class="nav">
    <a style="left:412px">HIV TREATMENT</a>
    <a style="left:566px">HIV &amp; NUTRITION</a>
    <a style="left:731px">HIV &amp; EXERCISE</a>
  </nav>
  <a class="btn btn-outline contact-btn">Contact Us &rarr;</a>
</header>

<section class="stats">
  <div class="stat-icon" style="left:118px">
    <svg width="40" height="40" viewBox="0 0 40 40"><circle cx="20" cy="10" r="6" fill="#A7469A"/><path d="M8 34c0-8 5-14 12-14s12 6 12 14z" fill="#6B429C"/></svg>
  </div>
  <div class="stat-num" style="left:230px">100+</div>
  <div class="stat-label" style="left:230px">Total resource</div>

  <div class="stat-icon" style="left:481px">
    <svg width="40" height="40" viewBox="0 0 40 40"><circle cx="20" cy="11" r="7" fill="#A7469A"/><path d="M6 36c0-9 6-15 14-15s14 6 14 15z" fill="#6B429C"/><circle cx="14" cy="30" r="3" fill="#fff"/></svg>
  </div>
  <div class="stat-num" style="left:595px">50+</div>
  <div class="stat-label" style="left:595px">Expert Mentor</div>

  <div class="stat-icon" style="left:845px">
    <svg width="40" height="40" viewBox="0 0 40 40"><circle cx="18" cy="11" r="7" fill="#6B429C"/><path d="M4 36c0-9 6-15 14-15s14 6 14 15z" fill="#6B429C"/><circle cx="30" cy="28" r="6" fill="#A7469A"/></svg>
  </div>
  <div class="stat-num" style="left:958px">300+</div>
  <div class="stat-label" style="left:958px">Patient Joined</div>
</section>

<section class="about">
  <div class="abs eyebrow-line"></div>
  <div class="abs eyebrow">About us</div>
  <h2>Sed Quia Non<br>Numqu Eius Modi<br>Tempora.</h2>
  <p class="para">Excepteur sint occaecat cupidatat non proident, sunt in culpa qui officia deserunt mollit anim id est laborum. Sed ut perspi under it omnis iste natus error sit voluptatem accusantium doloremquesit laudantium, totam rem aperiam, eaque ipsa quae ab illo inventos veritatis et quasi architecto beatae vitae dicta sunt explicabo pro Nemo enim ipsam voluptatem.</p>
</section>

<section class="treatment">
  <div class="frame"></div>
  <div class="photo" role="img" aria-label="Stethoscope beside an open hand holding a red awareness ribbon on a grey surface"></div>
  <h2>HIV Treatment</h2>
  <p class="para">Lorem ipsum dolor sit amet, consectetur adipisic elit sed do eiusmod tempor incididunt ut labores etos se dolore magna aliqua. Ut enim ad minim veni quis pto nostrud exercitation ullamco laboris nisi utis aliquipo ex ea commodo consequat. Duis aute sed dolor insis reprehenderit in voluptate.</p>
  <a class="btn">View More &rarr;</a>
</section>

<section class="nutrition">
  <div class="photo nutrition-photo" role="img" aria-label="Smiling woman eating a carrot stick and holding a bowl of fresh vegetables, with purple geometric shapes"></div>
  <div class="dot" style="left:1096px;top:230px;width:42px;height:42px"></div>
  <div class="badge">Insprimg<small>Healthy</small>Living</div>
  <h2>HIV and Nutrition</h2>
  <p class="para">Lorem ipsum dolor sit amet, consectetur adipisic elit sed do eiusmod tempor incididunt ut labores etos se dolore magna aliqua. Ut enim ad minim veni quis pto nostrud exercitation ullamco.</p>
  <a class="btn">View More &rarr;</a>
</section>

<section class="exercise">
  <h2>HIV and Exercise</h2>
  <p class="para">Lorem ipsum dolor sit amet, consectetur adipisic elit sed do eiusmod tempor incididunt utsed.</p>
  <a class="btn btn-outline">View More &rarr;</a>
  <div class="photo exercise-photo" role="img" aria-label="Man doing a push-up with one leg raised on a blue exercise mat in a bright room"></div>
  <div class="daily">
    <svg width="46" height="46" viewBox="0 0 46 46" fill="none" stroke="#fff" stroke-width="2"><rect x="12" y="6" width="22" height="22" rx="3"/><path d="M23 11v12M17 17h12"/><path d="M4 30c6-2 10 0 14 3h10c2 0 2 3 0 3H18M4 38c8 2 16 2 26-4l10-6"/></svg>
    <div>Daily Need<br><small>For Your Beter</small><br>Health</div>
  </div>
  <ul class="check-list">
    <li><span class="arrow"><svg width="14" height="10" viewBox="0 0 14 10"><path d="M0 5h12M8 1l4 4-4 4" stroke="#fff" stroke-width="1.6" fill="none"/></svg></span>At vero eos et accusamus et iusto odio sid non provident procure.</li>
    <li><span class="arrow"><svg width="14" height="10" viewBox="0 0 14 10"><path d="M0 5h12M8 1l4 4-4 4" stroke="#fff" stroke-width="1.6" fill="none"/></svg></span>Quo minus id quod maxime placeat facere istar possimus omnis.</li>
    <li><span class="arrow"><svg width="14" height="10" viewBox="0 0 14 10"><path d="M0 5h12M8 1l4 4-4 4" stroke="#fff" stroke-width="1.6" fill="none"/></svg></span>Sapiente delectus ut aut reiciendis voluptatibus maiores alias.</li>
    <li><span class="arrow"><svg width="14" height="10" viewBox="0 0 14 10"><path d="M0 5h12M8 1l4 4-4 4" stroke="#fff" stroke-width="1.6" fill="none"/></svg></span>Nor again is there anyone who loves or pursues or desires to obtain.</li>
    <li><span class="arrow"><svg width="14" height="10" viewBox="0 0 14 10"><path d="M0 5h12M8 1l4 4-4 4" stroke="#fff" stroke-width="1.6" fill="none"/></svg></span>Laborious physical exercise, except to obtain advantage.</li>
    <li><span class="arrow"><svg width="14" height="10" viewBox="0 0 14 10"><path d="M0 5h12M8 1l4 4-4 4" stroke="#fff" stroke-width="1.6" fill="none"/></svg></span>Pleasure that has no annoying consequences, or one who avoids.</li>
  </ul>
</section>

<section class="mentors">
  <h2>Our Expert Mentor</h2>
  <p class="lead">Adipisci velit sed quia non numquam eius modi tempora incidu<br>labore et dolore magnam aliquam quaerat voluptatem</p>
  <svg class="slider-arrow" style="left:84px" width="20" height="40" viewBox="0 0 20 40"><path d="M18 2L2 20l16 18" stroke="#fff" stroke-opacity=".7" stroke-width="2" fill="none"/></svg>
  <svg class="slider-arrow" style="left:1094px" width="20" height="40" viewBox="0 0 20 40"><path d="M2 2l16 18L2 38" stroke="#fff" stroke-opacity=".7" stroke-width="2" fill="none"/></svg>
  <div class="mentor" style="left:139px"><div class="avatar-ring"><div class="avatar" role="img" aria-label="Portrait of a mentor in a white coat"></div></div><div class="mentor-name">Dr. Owen Hale</div><div class="mentor-role">HIV Mentor</div><div class="mentor-rule"></div></div>
  <div class="mentor" style="left:367px"><div class="avatar-ring"><div class="avatar" role="img" aria-label="Portrait of a mentor in blue scrubs"></div></div><div class="mentor-name">Dr. Mira Stone</div><div class="mentor-role">HIV Mentor</div><div class="mentor-rule"></div></div>
  <div class="mentor" style="left:593px"><div class="avatar-ring"><div class="avatar" role="img" aria-label="Portrait of a mentor in a white coat"></div></div><div class="mentor-name">Dr. Felix Rowe</div><div class="mentor-role">HIV Mentor</div><div class="mentor-rule"></div></div>
  <div class="mentor" style="left:831px"><div class="avatar-ring"><div class="avatar" role="img" aria-label="Portrait of a mentor in a white coat"></div></div><div class="mentor-name">Dr. Lena Brooks</div><div class="mentor-role">HIV Mentor</div><div class="mentor-rule"></div></div>
</section>

<section class="consult">
  <div class="frame"></div>
  <div class="photo" role="img" aria-label="Young woman in a white t-shirt holding a red awareness ribbon"></div>
  <h2>Get a Free<br>Consulting Now</h2>
  <p class="para">Quis nostrud exercitation ullamco laboris nisi ut aliquip ex ea commodo consequat.</p>
  <form class="form-card">
    <label class="field-label" style="left:29px;top:39px">Your Name</label>
    <div class="field" style="left:29px;top:61px;width:222px;height:51px">John Lobo</div>
    <label class="field-label" style="left:265px;top:39px">Your Email</label>
    <div class="field" style="left:265px;top:61px;width:220px;height:51px">john@email.com</div>
    <label class="field-label" style="left:29px;top:151px">Phone No</label>
    <div class="field" style="left:29px;top:172px;width:222px;height:52px">1234567890</div>
    <label class="field-label" style="left:265px;top:151px">Subject</label>
    <div class="field" style="left:265px;top:172px;width:220px;height:52px;justify-content:space-between;padding-right:18px">HIV<svg width="12" height="8" viewBox="0 0 12 8"><path d="M1 1l5 5 5-5" stroke="#666" stroke-width="1.5" fill="none"/></svg></div>
    <label class="field-label" style="left:29px;top:263px">Message</label>
    <div class="field area" style="left:29px;top:286px;width:456px;height:169px">Leave a mesage</div>
    <a class="btn">Send Mesage &rarr;</a>
  </form>
</section>

<footer class="site-footer">
  <div class="brand"><span class="brand-mark"></span><span class="brand-name">Inform<b>HIV</b></span></div>
  <span class="social" style="left:85px" aria-label="Social link"></span>
  <span class="social" style="left:148px" aria-label="Social link"></span>
  <span class="social" style="left:211px" aria-label="Social link"></span>

  <div class="foot-title" style="left:338px">Quick Links</div>
  <div class="foot-links">
    <a style="left:338px;top:142px">HIV Treatment</a>
    <a style="left:338px;top:175px">HIV &amp; Nutrition</a>
    <a style="left:338px;top:208px">HIV &amp; Exercise</a>
    <a style="left:338px;top:241px">Contact Us</a>
  </div>

  <div class="foot-title" style="left:550px">Contact Info</div>
  <svg class="foot-icon" style="left:550px;top:149px" width="18" height="14" viewBox="0 0 18 14"><rect width="18" height="14" rx="2" fill="#A7469A"/><path d="M1 2l8 6 8-6" stroke="#1B1228" stroke-width="1.5" fill="none"/></svg>
  <div class="foot-text" style="left:583px;top:142px">info@example.com</div>
  <svg class="foot-icon" style="left:550px;top:198px" width="18" height="18" viewBox="0 0 24 24"><path d="M6.6 10.8a15 15 0 006.6 6.6l2.2-2.2a1 1 0 011-.25 11.4 11.4 0 003.6.57 1 1 0 011 1V20a1 1 0 01-1 1A17 17 0 013 4a1 1 0 011-1h3.5a1 1 0 011 1c0 1.25.2 2.45.57 3.6a1 1 0 01-.25 1z" fill="#A7469A"/></svg>
  <div class="foot-text" style="left:583px;top:194px">123-456-7890</div>
  <svg class="foot-icon" style="left:551px;top:248px" width="16" height="22" viewBox="0 0 16 22"><path d="M8 0a8 8 0 00-8 8c0 6 8 14 8 14s8-8 8-14a8 8 0 00-8-8z" fill="#A7469A"/><circle cx="8" cy="8" r="3" fill="#1B1228"/></svg>
  <div class="foot-text" style="left:583px;top:244px">Some line goes here<br>New York</div>

  <div class="foot-title" style="left:841px">Newsletter</div>
  <div class="foot-text" style="left:841px;top:144px;width:280px">Ab illo inventore veritatis etosi quasi architecto beatae</div>
  <div class="news-field">
    <svg width="16" height="12" viewBox="0 0 16 12"><rect width="16" height="12" rx="1.5" fill="#8a8296"/><path d="M1 1.5l7 5 7-5" stroke="#2b2239" stroke-width="1.4" fill="none"/></svg>
    Your email
    <svg style="margin-left:auto;margin-right:18px" width="18" height="18" viewBox="0 0 18 18"><path d="M1 8L17 1l-6 16-3-7z" fill="#A7469A"/></svg>
  </div>

  <div class="foot-rule"></div>
  <div class="to-top"><svg width="14" height="10" viewBox="0 0 14 10"><path d="M1 9l6-7 6 7" stroke="#fff" stroke-width="2" fill="none"/></svg></div>
  <div class="copyright">Copyright © 2023 Company Name. All rights reserved.</div>
</footer>

</body>
</html>
```